Sleep/Snoring Business - Requires Website - Australia

We are seeking a simple to maintain website for our sleep business. The health care business provides diagnostic and treatment solutions for snoring, sleep disorders and other respiratory problems.

Ideally, colours to match the company logo (attached).

The page must be built using WORDPRESS.

Ideally site will have a home page outlining the business, with 5 sub pages - being "Diagnosis" "Treatment Options", "Prodcuts", "About Us", "Contact Us"

The site home page should include a large picture on the home page.

The "Treatment Options" and "Diagnosis" pages must include:
Allow for a few pictures with assocaited text, plus space for some embeded youtube videos.

"Prodcuts" page should have the ability to show 3-4 products across the page with text below.. that can include external URL to products

The "About Us" page must include:
1. a Map (google map) to identify the various locations. There are 6 in total.
2. A Section to describe our doctors/staff - allow for a picture and some text

The "Contact Us" page must include:
email form
telephone details

The overall design should have a clean and medical/safe feeling

Target Market(s)

People who snore and those with sleeping and respiratory disorders

Industry/Entity Type

Health Care

Coding

Coded - Design and coding required

Number of Pages Required

5+ page

Colors

Designer to choose colors to be used in the design.

Requirements
Must have
• The page must be built using WORDPRESS.
• Ideally site will have a home page outlining the business, with 5 sub pages - being "Diagnosis" "Treatment Options", "Prodcuts", "About Us", "Contact Us"
• The site home page should include a large picture on the home page.
• The "Treatment Options" and "Diagnosis" pages must include:
• Allow for a few pictures with assocaited text, plus space for some embeded youtube videos.
• "Prodcuts" page should have the ability to show 3-4 products across the page with text below.. that can include external URL to products
• The "About Us" page must include:
• 1. a Map (google map) to identify the various locations. There are 6 in total.
• 2. A Section to describe our doctors/staff - allow for a picture and some text
• The "Contact Us" page must include:
• email form
• telephone details
• Pictures must be licenced or free to use
Nice to have
• Home page pictures showing people sleeping well, snoring or fresh air (landscape) type transition pictures (at least 3).
Should not have
• Not to look cheap
• This is a high end healthcare business, so must look that way

```html
<!DOCTYPE html>
<html lang="en">
<head>
<meta charset="utf-8">
<title>Dreamfield Australia – Home</title>
<link href="https://fonts.googleapis.com/css2?family=Catamaran:wght@500;600;700&family=Roboto+Condensed:wght@700&family=Arimo:wght@400;700&display=swap" rel="stylesheet">
<style>
  :root{
    --brand-navy:#134a7c;
    --brand-deep:#0f3f6e;
    --brand-accent:#1f5da0;
    --band-light:#8fadd6;
    --button:#5b8fd0;
    --text-dark:#222;
    --text-muted:#333;
    --white:#fff;
    --rule:rgba(255,255,255,.35);
  }
  *{box-sizing:border-box;margin:0;padding:0}
  html,body{width:1200px;height:825px;overflow:hidden;background:var(--white)}
  body{position:relative;font-family:"Arimo",Arial,sans-serif;color:var(--text-dark)}
  a{color:inherit;text-decoration:none}

  .site-header{position:absolute;left:0;top:0;width:1200px;height:111px;background:var(--white)}
  .brand{position:absolute;left:161px;top:24px;display:flex;align-items:center;gap:9px;color:var(--brand-navy);font-family:"Catamaran",sans-serif;font-weight:700}
  .brand-dot{width:15px;height:15px;border-radius:50%;background:var(--brand-navy)}
  .brand-name{display:block;font-size:34px;line-height:34px}
  .brand-sub{display:block;font-size:11px;letter-spacing:5px;line-height:15px;margin-left:3px}

  .top-contact{position:absolute;top:8px;height:26px;display:flex;align-items:center;gap:8px;font-family:"Arimo",sans-serif;font-weight:700;font-size:14px;color:var(--text-dark);white-space:nowrap}
  .top-contact svg{width:24px;height:24px;flex:none}
  .top-contact.email{right:317px}
  .top-contact.phone{left:913px}
  .top-divider{position:absolute;left:897px;top:6px;width:1px;height:30px;background:#d5d5d5}

  .main-nav{position:absolute;top:65px;right:163px;display:flex;align-items:center;font-family:"Catamaran",sans-serif;font-weight:600;font-size:14.5px;color:var(--text-dark);white-space:nowrap}
  .main-nav a{padding:0 15px;line-height:22px;border-left:1px solid #ccc}
  .main-nav a:first-child{padding-left:0;border-left:none}
  .main-nav a:last-child{padding-right:0}
  .main-nav a.is-current{color:var(--brand-accent)}

  .hero{position:absolute;left:0;top:111px;width:1200px;height:446px;
    background:linear-gradient(100deg,#8a6a55 0%,#c7b3a4 22%,#ebe6e2 45%,#f1eeec 62%,#e0c6b5 80%,#b1674a 100%)}
  .hero-caption{position:absolute;left:0;bottom:0;width:100%;height:57px;background:rgba(40,40,40,.55);display:flex;align-items:center;justify-content:center}
  .hero-caption h1{font-family:"Roboto Condensed",sans-serif;font-weight:700;font-size:27px;color:var(--white);white-space:nowrap}
  .hero-arrow{position:absolute;top:14px;width:20px;height:30px}
  .hero-arrow.prev{left:60px}
  .hero-arrow.next{left:1100px}

  .site-footer{position:absolute;left:0;top:557px;width:1200px;height:225px;background:var(--brand-navy);color:var(--white)}
  .footer-col{position:absolute;top:30px}
  .footer-col h2{font-family:"Catamaran",sans-serif;font-weight:600;font-size:16px;line-height:20px;padding-bottom:8px;border-bottom:1px solid var(--rule)}
  .col-links{left:161px;width:100px}
  .col-contact{left:353px;width:192px}
  .col-inquiry{left:637px;width:208px}
  .col-follow{left:939px;width:100px}
  .col-sep{position:absolute;top:42px;width:1px;height:150px;background:rgba(255,255,255,.12)}

  .link-list{list-style:none;margin-top:14px;padding-left:1px;font-size:12px}
  .link-list li{line-height:20px}

  .contact-item{display:flex;gap:10px;font-size:10.5px;line-height:14px;color:#e8eef6;margin-top:16px;width:200px}
  .contact-item:first-of-type{margin-top:17px}
  .contact-item svg{flex:none;width:11px;height:12px;margin-top:1px}
  .contact-item.phone{margin-top:20px}
  .contact-item.mail{margin-top:21px}

  .inquiry-form{margin-top:16px}
  .inquiry-form .field{display:block;width:210px;height:18px;border:1px solid #c9d6e6;margin-bottom:4.5px;font-size:11px;line-height:16px;padding-left:5px;color:var(--white);margin-left:-2px}
  .inquiry-form .submit{display:inline-flex;align-items:center;gap:6px;margin-top:2px;margin-left:-2px;height:21px;padding:0 10px 0 12px;background:var(--button);font-weight:700;font-size:12px;color:var(--white)}

  .social-list{list-style:none;margin-top:15px}
  .social-list li{display:flex;align-items:center;gap:10px;height:18px;margin-bottom:13px;font-size:11px}
  .social-list .marker{width:18px;height:18px;background:#e9eef5}

  .copyright{position:absolute;left:0;top:782px;width:1200px;height:43px;background:var(--band-light);display:flex;align-items:center;justify-content:center;font-size:11.5px;color:var(--text-muted)}
</style>
</head>
<body>

<header class="site-header">
  <a class="brand" href="#">
    <span class="brand-dot"></span>
    <span><span class="brand-name">Dreamfield</span><span class="brand-sub">AUSTRALIA</span></span>
  </a>

  <div class="top-contact email">
    <svg viewBox="0 0 26 26"><circle cx="13" cy="13" r="12" fill="none" stroke="#1f5da0" stroke-width="1.5"/><rect x="7" y="9" width="12" height="8" fill="#1f5da0"/><path d="M7 9l6 5 6-5" fill="none" stroke="#fff" stroke-width="1.2"/></svg>
    <span>info@dreamfieldclinic.com</span>
  </div>
  <div class="top-divider"></div>
  <div class="top-contact phone">
    <svg viewBox="0 0 26 26"><circle cx="13" cy="13" r="12" fill="none" stroke="#1f5da0" stroke-width="1.5"/><path d="M9 7c-1.5 1-1.8 3-.5 5.5 1.6 3 3.8 5.3 6.3 6.4 1.8.8 3 .3 3.7-.8l-2.3-2.2-1.6 1c-1.4-.7-3-2.4-3.7-3.9l1-1.6z" fill="#1f5da0"/></svg>
    <span>012-555-0147</span>
  </div>

  <nav class="main-nav">
    <a class="is-current" href="#">Home</a>
    <a href="#">Diagnosis</a>
    <a href="#">Treatment Options</a>
    <a href="#">Prodcuts</a>
    <a href="#">About Us</a>
    <a href="#">Contact Us</a>
  </nav>
</header>

<section class="hero" role="img" aria-label="Photo of a woman sleeping peacefully in a bed with white pillows and sheets">
  <div class="hero-caption">
    <svg class="hero-arrow prev" viewBox="0 0 20 30"><path d="M15 3L4 15l11 12" fill="none" stroke="#c8c8c8" stroke-width="2.5"/></svg>
    <h1>We Are Seeking A Simple To Maintain Website For Our Sleep Busines</h1>
    <svg class="hero-arrow next" viewBox="0 0 20 30"><path d="M5 3l11 12L5 27" fill="none" stroke="#c8c8c8" stroke-width="2.5"/></svg>
  </div>
</section>

<footer class="site-footer">
  <div class="footer-col col-links">
    <h2>Quick Links</h2>
    <ul class="link-list">
      <li><a href="#">Home</a></li>
      <li><a href="#">Diagnosis</a></li>
      <li><a href="#">Treatment Options</a></li>
      <li><a href="#">Prodcuts</a></li>
      <li><a href="#">About Us</a></li>
      <li><a href="#">Contact Us</a></li>
    </ul>
  </div>
  <div class="col-sep" style="left:306px"></div>

  <div class="footer-col col-contact">
    <h2>Contact Details</h2>
    <div class="contact-item">
      <svg viewBox="0 0 11 12"><path d="M5.5 0A4 4 0 0 0 1.5 4c0 3 4 8 4 8s4-5 4-8a4 4 0 0 0-4-4zm0 5.6a1.6 1.6 0 1 1 0-3.2 1.6 1.6 0 0 1 0 3.2z" fill="#fff"/></svg>
      <span>Lorem ipsum dolor sit consectetuer<br>adipiscing elit,&nbsp; diam nonummy<br>nibh Street No 5, zip Code: 897410</span>
    </div>
    <div class="contact-item phone">
      <svg viewBox="0 0 11 12"><path d="M2.5 0C1 .8.6 2.5 1.8 5c1.3 2.8 3.5 5 5.8 6.4 1.4.8 2.6.5 3.2-.6L8.7 8.8 7.4 9.7C6.2 9 4.6 7.2 3.9 5.8l1-1.4z" fill="#fff"/></svg>
      <span>012-555-0147</span>
    </div>
    <div class="contact-item mail">
      <svg viewBox="0 0 11 12"><rect x="0" y="3" width="11" height="7" fill="#fff"/><path d="M0 3l5.5 4L11 3" fill="none" stroke="#134a7c" stroke-width="1"/></svg>
      <span>info@dreamfieldclinic.com</span>
    </div>
  </div>
  <div class="col-sep" style="left:591px"></div>

  <div class="footer-col col-inquiry">
    <h2>Quick Inquiry</h2>
    <form class="inquiry-form">
      <span class="field">Your Name</span>
      <span class="field">Email</span>
      <span class="field">Phone</span>
      <span class="field">Message</span>
      <span class="submit">SUBMIT <svg width="5" height="8" viewBox="0 0 5 8"><path d="M0 0l5 4-5 4z" fill="#fff"/></svg></span>
    </form>
  </div>
  <div class="col-sep" style="left:892px"></div>

  <div class="footer-col col-follow">
    <h2>Follow Us</h2>
    <ul class="social-list">
      <li><span class="marker"></span>Chatterbox</li>
      <li><span class="marker"></span>Birdsong</li>
      <li><span class="marker"></span>Circles</li>
      <li><span class="marker"></span>WorkNet</li>
    </ul>
  </div>
</footer>

<div class="copyright">Copyright© 2017 Dreamfield Australia. All right reserved.</div>

</body>
</html>
```